Semaglutide Diet

A flyer design for a weight loss program based on the peptide Semaglutide that our clinic is rolling out. Here are some very rough ideas

```html
<!DOCTYPE html>
<html lang="en">
<head>
<meta charset="utf-8">
<title>Semaglutide Diet – Weight Loss Program Flyer</title>
<link rel="stylesheet" href="https://fonts.googleapis.com/css2?family=Fira+Sans+Condensed:wght@300;500;600&display=swap">
<style>
  :root{
    --backdrop:#3a3938;
    --paper:#f8efeb;
    --bronze:#ad7f62;
    --pink:#ec8fbd;
    --ink:#1c1c1c;
    --body-grey:#5b5b5b;
    --contact-grey:#555555;
    --photo-dark:#1c1f1f;
    --skin:#d7a98c;
  }
  *{margin:0;padding:0;box-sizing:border-box}
  html,body{width:1156px;height:1200px;overflow:hidden;background:var(--backdrop)}
  body{font-family:"Fira Sans Condensed",sans-serif;position:relative}
  .flyer{position:absolute;left:129px;top:129px;width:904px;height:904px;background:var(--paper);overflow:hidden}
  .flyer-art{position:absolute;inset:0;width:904px;height:904px}
  .headline{position:absolute;left:52px;font-size:69px;font-weight:600;line-height:1;color:var(--bronze);letter-spacing:0.5px;white-space:nowrap}
  .headline.l1{top:69px}
  .headline.l2{top:151px}
  .headline.l3{top:235px}
  .subhead{position:absolute;left:52px;top:318px;font-size:39px;font-weight:600;line-height:1;color:var(--pink);white-space:nowrap}
  .question{position:absolute;left:52px;font-size:33px;font-weight:600;line-height:1;white-space:nowrap}
  .question.results{top:431px;color:var(--ink)}
  .question.want{top:473px;color:var(--bronze)}
  .benefits{list-style:none;position:absolute;left:50px;top:539px}
  .benefits li{display:flex;align-items:center;height:33px;margin-bottom:34px;font-size:33px;font-weight:300;line-height:1;color:var(--body-grey);white-space:nowrap}
  .benefits svg{width:24px;height:24px;margin-right:12px;flex:none}
  .contact{position:absolute;right:35px;top:739px;text-align:right;line-height:1}
  .contact .label{font-size:28px;font-weight:600;color:var(--ink);margin-bottom:7px}
  .contact p{font-size:28px;font-weight:500;color:var(--contact-grey);margin-bottom:7px}
</style>
</head>
<body>
<div class="flyer">
  <svg class="flyer-art" viewBox="0 0 1098 1098" preserveAspectRatio="none">
    <defs>
      <radialGradient id="bodyTone" cx="0.55" cy="0.45" r="0.55">
        <stop offset="0" stop-color="var(--skin)"/>
        <stop offset="0.6" stop-color="#b98a70"/>
        <stop offset="1" stop-color="var(--photo-dark)"/>
      </radialGradient>
      <linearGradient id="silver" x1="0" y1="0" x2="1" y2="0.3">
        <stop offset="0" stop-color="#b9b9b9"/>
        <stop offset="0.45" stop-color="#f2f2f2"/>
        <stop offset="0.7" stop-color="#e6e6e6"/>
        <stop offset="1" stop-color="#bdbdbd"/>
      </linearGradient>
    </defs>
    <path class="pink-band" fill="var(--pink)" d="M728,0 C600,180 530,380 558,600 C580,800 640,980 688,1098 L1098,1098 L1098,0 Z"/>
    <path class="hero-photo" role="img" aria-label="Photo of a woman in a white bikini measuring her waist with a pink tape measure, molecule models behind" fill="url(#bodyTone)" d="M745,0 C625,180 560,380 565,600 C575,780 615,900 650,955 C840,915 990,800 1098,600 L1098,0 Z"/>
    <path class="contact-panel" fill="url(#silver)" d="M635,985 C820,950 990,840 1098,660 L1098,1098 L688,1098 C665,1060 648,1020 635,985 Z"/>
  </svg>

  <h1 class="headline l1">WEIGHT LOSS</h1>
  <div class="headline l2">PROGRAM</div>
  <div class="headline l3">BASED ON</div>
  <h2 class="subhead">SEMAGLUTIDE DIET</h2>

  <div class="question results">DO YOU WANT RESULTS?</div>
  <div class="question want">DO YOU WANT TO:</div>

  <ul class="benefits">
    <li><svg viewBox="0 0 24 24"><polygon points="12,1.5 21.5,7 21.5,17 12,22.5 2.5,17 2.5,7" fill="none" stroke="var(--bronze)" stroke-width="1.6"/></svg>Lose 5 pounds or more</li>
    <li><svg viewBox="0 0 24 24"><polygon points="12,1.5 21.5,7 21.5,17 12,22.5 2.5,17 2.5,7" fill="none" stroke="var(--bronze)" stroke-width="1.6"/></svg>Improve your metabolism</li>
    <li><svg viewBox="0 0 24 24"><polygon points="12,1.5 21.5,7 21.5,17 12,22.5 2.5,17 2.5,7" fill="none" stroke="var(--bronze)" stroke-width="1.6"/></svg>Have more energy</li>
    <li><svg viewBox="0 0 24 24"><polygon points="12,1.5 21.5,7 21.5,17 12,22.5 2.5,17 2.5,7" fill="none" stroke="var(--bronze)" stroke-width="1.6"/></svg>Lose water weight</li>
    <li><svg viewBox="0 0 24 24"><polygon points="12,1.5 21.5,7 21.5,17 12,22.5 2.5,17 2.5,7" fill="none" stroke="var(--bronze)" stroke-width="1.6"/></svg>Improve overall health</li>
  </ul>

  <div class="contact">
    <div class="label">CONTACT</div>
    <p>012 345 6789</p>
    <p>Mail @email.com</p>
    <p>website.com</p>
  </div>
</div>
</body>
</html>
```